Business card for new business - financial management

I need a business card designed for my new business. I'm the owner / sole trader of TVH Consulting, which provides financial management services for Government. I'd like the design to incorporate the attached business name and colours. The design should include colour and not be too way out - it needs to look at home in a government environment.
Details to be included on the card are:
TVH Consulting
Delia Ravick
0400 938 214
deliaeravick@mailbrook.net
47 Pellham Crescent, Curtin ACT 2605
Single or double sided designs would be good.
Target Market(s)
Employees at Australian Federal Government agencies
Industry/Entity Type
Government
Look and feel

```html
<!DOCTYPE html>
<html lang="en">
<head>
<meta charset="UTF-8">
<title>TVH Consulting – Business Card</title>
<link rel="stylesheet" href="https://fonts.googleapis.com/css2?family=Ubuntu:wght@400;500&display=swap">
<style>
  :root {
    --teal-dark: #14627a;
    --blue-mid: #1592c2;
    --blue-light: #7fd4ee;
    --blue-pale: #86cde4;
    --navy: #1d4f91;
    --white: #ffffff;
    --ink: #1f3f66;
    --backdrop: #eef1f4;
  }
  * { margin: 0; padding: 0; box-sizing: border-box; }
  html, body {
    width: 1200px; height: 676px; overflow: hidden;
    background: var(--backdrop);
    font-family: "Ubuntu", Arial, sans-serif;
  }
  .canvas { position: relative; width: 1200px; height: 676px; }
  .card {
    position: absolute;
    width: 520px; height: 300px;
    background: var(--white);
    overflow: hidden;
    box-shadow: 0 6px 18px rgba(20, 40, 60, 0.18);
  }
  .card--front { left: 50px; top: 130px; }
  .card--back { left: 630px; top: 250px; }

  .segment-bar { position: absolute; left: 0; width: 100%; display: flex; gap: 3px; }
  .segment-bar span { display: block; height: 100%; }
  .card--front .segment-bar { top: 0; height: 40px; }
  .card--front .seg-dark { width: 57%; background: var(--teal-dark); }
  .card--front .seg-mid { width: 19%; background: var(--blue-mid); }
  .card--front .seg-light { flex: 1; background: var(--blue-light); }
  .card--back .segment-bar { bottom: 0; height: 40px; }
  .card--back .seg-dark { width: 40%; background: var(--teal-dark); }
  .card--back .seg-mid { width: 43%; background: var(--blue-mid); }
  .card--back .seg-light { flex: 1; background: var(--blue-pale); }

  .wave { position: absolute; left: 0; bottom: 0; width: 100%; height: 110px; }

  .brand-name {
    position: absolute;
    font-weight: 500;
    white-space: nowrap;
    letter-spacing: 0.5px;
  }
  .card--front .brand-name {
    left: 60px; top: 108px;
    font-size: 50px; color: var(--navy);
  }

  .brand-band {
    position: absolute; left: 0; top: 0;
    width: 100%; height: 118px;
    background: var(--blue-mid);
  }
  .card--back .brand-name {
    left: 0; right: 0; top: 38px; text-align: center;
    font-size: 36px; color: var(--white);
  }

  .holder-name {
    position: absolute; left: 0; right: 0; top: 128px;
    text-align: center;
    font-size: 21px; font-weight: 500; color: var(--ink);
  }
  .contact-list {
    position: absolute; left: 160px; top: 164px;
    list-style: none;
  }
  .contact-list li {
    display: flex; align-items: center;
    height: 23px; margin-bottom: 2px;
    font-size: 11px; color: var(--navy);
  }
  .contact-icon {
    width: 15px; height: 15px; margin-right: 14px; flex: none;
  }
</style>
</head>
<body>
<main class="canvas">

  <section class="card card--front" aria-label="Business card front">
    <div class="segment-bar">
      <span class="seg-dark"></span><span class="seg-mid"></span><span class="seg-light"></span>
    </div>
    <div class="brand-name">TVH Consulting</div>
    <svg class="wave" viewBox="0 0 520 110" preserveAspectRatio="none" aria-hidden="true">
      <path d="M0 30 C120 48 220 52 330 34 C410 22 470 14 520 12 L520 110 L0 110 Z" fill="var(--teal-dark)"/>
      <path d="M0 24 C120 42 220 46 330 28 C410 16 470 8 520 6" fill="none" stroke="var(--blue-light)" stroke-width="3"/>
    </svg>
  </section>

  <section class="card card--back" aria-label="Business card back">
    <div class="brand-band"></div>
    <div class="brand-name">TVH Consulting</div>
    <div class="holder-name">Delia Ravick</div>
    <ul class="contact-list">
      <li>
        <svg class="contact-icon" viewBox="0 0 16 16" aria-hidden="true">
          <circle cx="8" cy="8" r="8" fill="var(--blue-mid)"/>
          <path d="M8 3.5a2.7 2.7 0 0 0-2.7 2.7C5.3 8.3 8 12 8 12s2.7-3.7 2.7-5.8A2.7 2.7 0 0 0 8 3.5z" fill="var(--white)"/>
          <circle cx="8" cy="6.2" r="1" fill="var(--blue-mid)"/>
        </svg>
        47 Pellham Crescent, Brindlewood QX 2911
      </li>
      <li>
        <svg class="contact-icon" viewBox="0 0 16 16" aria-hidden="true">
          <circle cx="8" cy="8" r="8" fill="var(--blue-mid)"/>
          <path d="M5.2 4.2l1.5-.4 1 2.2-1 .8c.5 1.1 1.3 1.9 2.4 2.4l.8-1 2.2 1-.4 1.5c-3.4.2-6.7-3.1-6.5-6.5z" fill="var(--white)"/>
        </svg>
        0400 938 214
      </li>
      <li>
        <svg class="contact-icon" viewBox="0 0 16 16" aria-hidden="true">
          <circle cx="8" cy="8" r="8" fill="var(--blue-mid)"/>
          <rect x="4" y="5.2" width="8" height="5.6" rx="0.6" fill="var(--white)"/>
          <path d="M4.3 5.6L8 8.4l3.7-2.8" fill="none" stroke="var(--blue-mid)" stroke-width="0.9"/>
        </svg>
        deliaeravick@mailbrook.net
      </li>
    </ul>
    <div class="segment-bar">
      <span class="seg-dark"></span><span class="seg-mid"></span><span class="seg-light"></span>
    </div>
  </section>

</main>
</body>
</html>
```